QRV Supplements needs a label designer for supplement company

Looking for an on going label designer for my supplement company. I have three products that will need designs. I'm about to launch my sleep supplement called Velora Rest and that's the first design needed.
I would like all designs to be somewhat simple, not overstated and uniformed so that when you look at all of the labels of the different supplements they are similar and you can tell it's the same brand.
Please see attached sample pictures below as ideas.
Updates

The brand is QRV supplements, logo file has been provided. The supplement is called Velora Rest. It is a liquid supplement that is a 32/33 ounce white bottle. Die lines and measurements will be provided. Here's text for wording ideas: Wording: Natural Sleep Aid Reset your circadian rhythm. May help you: Fall asleep faster. Get a deeper more restful sleep. Boost Immune System Remember your dreams. Protect your brain and flush toxins. Wake up feeling refreshed. Non-gmo Gluten Free Sugar Free Vegan Manufactured in cGMP factory Manufactured in USA

Target Market(s)

Health and wellness/supplement industry for regular people not hardcore gym goers. My supplements are for a health lifestyle not bodybuilding.

Industry/Entity Type

Health And Wellness

Colors
3176b5
3276b5
33a6d7
85cae6
85abd2
cedeed
e4daeb
b7a5cd

Requirements
Must have
• There will be some text and wording that I will provide that must be on the bottles.

```html
<!DOCTYPE html>
<html lang="en">
<head>
<meta charset="utf-8">
<title>Velora Rest — QRV Supplements Label</title>
<link rel="stylesheet" href="https://fonts.googleapis.com/css2?family=Exo+2:wght@400;500;700&display=swap">
<style>
  :root {
    --stage: #bfc0c3;
    --label-deep: #173f8c;
    --label-mid: #2356ad;
    --label-light: #3176b5;
    --band-cyan: #33a6d7;
    --band-sky: #85cae6;
    --band-pale: #cedeed;
    --ink-light: #ffffff;
    --ink-soft: #cedeed;
    --ink-dark: #123a85;
    --art-glow: #3fb4ef;
  }
  * { margin: 0; padding: 0; box-sizing: border-box; }
  html, body {
    width: 1200px; height: 900px; overflow: hidden;
    background: var(--stage);
    font-family: "Exo 2", sans-serif;
  }
  .canvas { position: relative; width: 1200px; height: 900px; }
  .label {
    position: absolute; left: 263px; top: 20px;
    width: 673px; height: 860px; overflow: hidden;
    background: linear-gradient(160deg, var(--label-light) 0%, var(--label-mid) 40%, var(--label-deep) 100%);
  }
  .label-bands { position: absolute; inset: 0; width: 100%; height: 100%; }
  .head-art {
    position: absolute; left: 398px; top: 505px; width: 275px; height: 355px;
    background: radial-gradient(ellipse at 55% 35%, var(--art-glow) 0%, var(--label-light) 45%, rgba(35,86,173,0) 75%);
  }
  .brand {
    position: absolute; left: 44px; top: 138px;
    display: flex; align-items: center; gap: 20px;
  }
  .brand-mark {
    width: 78px; height: 78px; border-radius: 50%;
    background: var(--ink-light);
  }
  .brand-name {
    color: var(--ink-light); font-weight: 700; font-size: 44px;
    letter-spacing: 1px; text-transform: uppercase; white-space: nowrap;
  }
  .product-name {
    position: absolute; left: 40px; top: 276px;
    color: var(--ink-light); font-weight: 500; font-size: 100px;
    letter-spacing: 1px; line-height: 1;
  }
  .tagline {
    position: absolute; left: 52px; top: 420px;
    padding-left: 20px; border-left: 4px solid var(--ink-light);
    color: var(--ink-light); font-weight: 400; font-size: 30px; line-height: 1.15;
  }
  .tagline strong { font-weight: 500; }
  .benefits {
    position: absolute; left: 52px; top: 510px; width: 340px;
    list-style: none; color: var(--ink-soft);
    font-size: 20px; line-height: 27px;
  }
  .benefits-title { color: var(--ink-light); font-weight: 500; }
  .benefits li::before { content: "✓ "; color: var(--band-sky); }
  .benefits .benefits-title::before { content: none; }
  .certifications {
    position: absolute; left: 48px; top: 744px;
    color: var(--ink-dark); font-weight: 500; font-size: 17px; white-space: nowrap;
  }
  .origin {
    position: absolute; left: 48px; top: 770px;
    color: var(--ink-dark); font-weight: 400; font-size: 15px; white-space: nowrap;
  }
  .net-weight {
    position: absolute; left: 48px; top: 806px;
    color: var(--ink-dark); font-weight: 500; font-size: 32px;
  }
</style>
</head>
<body>
<main class="canvas">
  <section class="label">
    <svg class="label-bands" viewBox="0 0 673 860" preserveAspectRatio="none" aria-hidden="true">
      <polygon points="200,0 673,0 673,40 560,40 520,14 230,14" fill="var(--band-sky)" opacity="0.9"/>
      <polygon points="430,20 673,20 673,58 590,58 560,36 460,36" fill="var(--band-cyan)" opacity="0.7"/>
      <line x1="120" y1="40" x2="470" y2="40" stroke="var(--band-pale)" stroke-width="2" opacity="0.5"/>
      <polygon points="0,690 160,690 200,720 673,720 673,860 0,860" fill="var(--band-cyan)"/>
      <polygon points="0,730 180,730 215,760 673,760 673,860 0,860" fill="var(--band-sky)"/>
      <line x1="0" y1="700" x2="673" y2="700" stroke="var(--band-pale)" stroke-width="2" opacity="0.6"/>
    </svg>
    <div class="head-art" role="img" aria-label="Glowing blue illustration of a human head in profile with the brain visible"></div>
    <div class="brand">
      <span class="brand-mark"></span>
      <span class="brand-name">QRV Supplements</span>
    </div>
    <h1 class="product-name">Velora Rest</h1>
    <p class="tagline"><strong>Natural Sleep Aid</strong><br>Reset your circadian rhythm</p>
    <ul class="benefits">
      <li class="benefits-title">May help you:</li>
      <li>Fall asleep faster</li>
      <li>Get deeper, more restful sleep</li>
      <li>Boost your immune system</li>
      <li>Remember your dreams</li>
      <li>Wake up feeling refreshed</li>
    </ul>
    <p class="certifications">Non-GMO · Gluten Free · Sugar Free · Vegan</p>
    <p class="origin">Made in USA in a cGMP facility</p>
    <p class="net-weight">Nt wt. 30 mg</p>
  </section>
</main>
</body>
</html>
```